Post Card Design - Photo on front, details on back. Logo on both sides.

Back: See the photo of my old card. The back worked well, as it gave me lots of space to write on. The address details are still correct, but the logo has changed to Josephine Sans. Logo can be on one line or on two (if two, align it on the left).
Don't include the 'BEAUTIFUL WEDDING DRESSES...' bit.
I'd like to print this on thicker, slightly coarse paper, so don't go too small on detail.
Here are the Plume paper details: Paper Stock: Natural Uncoated
Paper Thickness: Premium
Finish: None
Front of Card: I'd like to see options for both pictures:
I think the painted image would look best with a frame in a pale shade and the logo in the frame fairly subtle.
The actual dress photo I'd like to see cropped a bit like in my mock up. You'll need to have a look at how the logo would be best placed on this. You can place it anywhere, or add a banner.
See my website for my brand's look: mirabeltoft.co.nz
Target Market(s)
Brides
Industry/Entity Type
Wedding Dresses
Contact Information for Business Card
Front: Photo and logo. Back: with details and lots of empty space. See attached photos for loose brief.
Other font styles liked:
- Josephine Sans
Requirements
Must have
- I hand-write the gown designs and price on the back of the card, so there needs to be plenty of empty space.
Nice to have
- As per brief.
Should not have
- It must look clean, romantic, modern. Timeless.

```html
<!DOCTYPE html>
<html lang="en">
<head>
<meta charset="utf-8">
<title>Mirabel Toft – Postcard</title>
<link href="https://fonts.googleapis.com/css2?family=Josefin+Sans:wght@300;400&display=swap" rel="stylesheet">
<style>
  :root {
    --backdrop: #c1c1c1;
    --paper: #ffffff;
    --ink: #676767;
    --ink-soft: #7a7a7a;
    --sand-light: #f7efe4;
    --sand: #efe1cd;
    --sand-deep: #e4cfb2;
    --card-shadow: rgba(0, 0, 0, 0.18);
  }

  * { box-sizing: border-box; margin: 0; padding: 0; }

  html, body {
    width: 1200px;
    height: 1000px;
    overflow: hidden;
  }

  body {
    position: relative;
    background: var(--backdrop);
    font-family: "Josefin Sans", sans-serif;
    color: var(--ink);
  }

  .postcard {
    position: absolute;
    background: var(--paper);
    box-shadow: 0 3px 8px var(--card-shadow);
    overflow: hidden;
  }

  .postcard--front {
    left: 32px;
    top: 72px;
    width: 684px;
    height: 482px;
    z-index: 2;
  }

  .postcard--back {
    left: 468px;
    top: 440px;
    width: 676px;
    height: 472px;
    z-index: 1;
  }

  .front-photo {
    position: absolute;
    top: 0;
    right: 0;
    width: 440px;
    height: 100%;
    background:
      linear-gradient(90deg,
        var(--paper) 0%,
        rgba(255, 255, 255, 0.85) 12%,
        rgba(255, 255, 255, 0.35) 30%,
        rgba(255, 255, 255, 0) 48%),
      linear-gradient(180deg,
        var(--sand-light) 0%,
        var(--sand) 55%,
        var(--sand-deep) 100%);
  }

  .wordmark {
    position: absolute;
    font-weight: 300;
    text-transform: uppercase;
    line-height: 1.02;
    letter-spacing: 0.06em;
    color: var(--ink);
  }

  .postcard--front .wordmark {
    left: 98px;
    top: 218px;
    font-size: 36px;
  }

  .postcard--back .wordmark {
    left: 34px;
    top: 368px;
    font-size: 27px;
  }

  .contact-details {
    position: absolute;
    right: 50px;
    bottom: 26px;
    list-style: none;
    text-align: right;
    font-weight: 300;
    font-size: 13px;
    line-height: 18px;
    letter-spacing: 0.12em;
    color: var(--ink-soft);
  }
</style>
</head>
<body>

  <section class="postcard postcard--front" aria-label="Postcard front">
    <div class="front-photo" role="img" aria-label="Photograph of a bride in an off-shoulder white satin mermaid gown standing in warm sunlight beside a pale stone colonnade"></div>
    <h1 class="wordmark">Mirabel<br>Toft</h1>
  </section>

  <section class="postcard postcard--back" aria-label="Postcard back">
    <p class="wordmark">Mirabel<br>Toft</p>
    <ul class="contact-details">
      <li>+64 9 412 5067</li>
      <li>mira@mirabeltoft.co.nz</li>
      <li>mirabeltoft.co.nz</li>
    </ul>
  </section>

</body>
</html>
```